Business card for auto dealership

Looking for a clean modern design.
Would like attached logo incorporated

Industry/Entity Type

Car dealership

Contact Information for Business Card

Name, website, phone, cell, fax, email

```html
<!DOCTYPE html>
<html lang="en">
<head>
<meta charset="utf-8">
<title>Halvern Truck &amp; Auto Sales – Business Card</title>
<link href="https://fonts.googleapis.com/css2?family=Arimo:wght@400;700&display=swap" rel="stylesheet">
<style>
  :root {
    --backdrop: #e8e8e8;
    --card: #303030;
    --card-edge: #262626;
    --ink: #ffffff;
    --ink-soft: #d9d9d9;
    --rule: #8a8a8a;
    --pattern-dark: #222222;
    --pattern-light: #4a4a4a;
  }
  * { box-sizing: border-box; margin: 0; padding: 0; }
  html, body {
    width: 1200px; height: 802px; overflow: hidden;
    background: var(--backdrop);
    font-family: "Arimo", Arial, sans-serif;
  }
  .stage {
    width: 1200px; height: 802px;
    display: flex; align-items: center; justify-content: center; gap: 60px;
  }
  .card {
    position: relative;
    width: 520px; height: 297px;
    background: var(--card);
    border: 1px solid var(--card-edge);
    color: var(--ink);
    overflow: hidden;
  }
  .brand {
    position: absolute; left: 44px; top: 96px;
    font-weight: 700; color: var(--ink);
    font-size: 40px; line-height: 1;
  }
  .brand .tagline { display: block; font-size: 11px; letter-spacing: 1.5px; margin-top: 6px; }
  .holder {
    position: absolute; left: 44px; top: 222px;
    font-size: 17px; letter-spacing: 1px; text-transform: uppercase;
  }
  .divider {
    position: absolute; left: 270px; top: 70px;
    width: 1px; height: 150px; background: var(--rule);
  }
  .contacts {
    position: absolute; left: 290px; top: 82px;
    list-style: none; font-size: 15px; color: var(--ink-soft);
  }
  .contacts li { display: flex; align-items: center; gap: 8px; height: 25px; white-space: nowrap; }
  .contacts svg { width: 13px; height: 13px; flex: none; fill: none; stroke: var(--ink); stroke-width: 1.6; }
  .pattern {
    position: absolute; inset: 0;
    background: linear-gradient(100deg, var(--pattern-dark) 0%, var(--card) 45%, var(--pattern-light) 100%);
  }
  .back .brand { left: auto; right: 40px; top: auto; bottom: 64px; font-size: 34px; text-align: left; }
  .back .brand .tagline { font-size: 10px; }
</style>
</head>
<body>
<main class="stage">
  <section class="card front">
    <div class="brand">Halvern<span class="tagline">TRUCK &amp; AUTO SALES</span></div>
    <p class="holder">Dana Halvern</p>
    <div class="divider"></div>
    <ul class="contacts">
      <li><svg viewBox="0 0 14 14"><path d="M3 1.5l2 2.5-1.2 1.5a7 7 0 0 0 4.7 4.7L10 9l2.5 2-1.5 2A10 10 0 0 1 1 3z"/></svg>555-014-2637</li>
      <li><svg viewBox="0 0 14 14"><rect x="3.5" y="1" width="7" height="12" rx="1"/><path d="M6 11h2"/></svg>555-019-8352</li>
      <li><svg viewBox="0 0 14 14"><rect x="1.5" y="6" width="11" height="6.5"/><path d="M4 6V1.5h6V6M4 9h6"/></svg>555-016-4908</li>
      <li><svg viewBox="0 0 14 14"><rect x="1" y="3" width="12" height="8"/><path d="M1 3l6 5 6-5"/></svg>dana@halvernauto.com</li>
      <li><svg viewBox="0 0 14 14"><circle cx="7" cy="7" r="5.8"/><path d="M1.2 7h11.6M7 1.2c-2.5 3-2.5 8.6 0 11.6M7 1.2c2.5 3 2.5 8.6 0 11.6"/></svg>www.halvernauto.com</li>
    </ul>
  </section>
  <section class="card back">
    <div class="pattern" role="img" aria-label="Embossed repeating monogram pattern in dark grey tones"></div>
    <div class="brand">Halvern<span class="tagline">TRUCK &amp; AUTO SALES</span></div>
  </section>
</main>
</body>
</html>
```